Design our industrial business landing pages

Welcome!

We have five landing pages that follow a very similar structure that I need fresh designs submitted for.

I have uploaded all of the files for entries to view and have made a structure for how I want the designs to generally look but PLEASE get CREATIVE.

I have made a short video to explain the project, please also view the google docs.

VIDEO

https://www.clipvane.com/share/a4f19c2e7b0d4e6f8a3c5d7e9b1f2a60?sid=f3b8d1e2-6a4c-4f7e-9b2d-1c5e8a7f3d90

OLD WEBSITE - https://www.marlowfield-pvc-solutions.co.uk/

DOCUMENT - https://docs.papernook.com/document/d/7kTq2Wx9LmPz4Rv8Ns3Bc6Yh1Jf5Gd0Ue2Ai4Oo7Xe/edit?usp=sharing

No one is following the design brief I set. All designers need to refer to this document. Not a single designer has followed this brief https://docs.papernook.com/document/d/7kTq2Wx9LmPz4Rv8Ns3Bc6Yh1Jf5Gd0Ue2Ai4Oo7Xe/edit?usp=sharing

```html
<!DOCTYPE html>
<html lang="en">
<head>
<meta charset="utf-8">
<title>Marlowfield PVC Solutions – Traxa Curtain</title>
<link rel="stylesheet" href="https://fonts.googleapis.com/css2?family=Inter:wght@400;500;600;700;800&display=swap">
<style>
:root{
  --crimson:#c63a51;
  --steel:#3a6f8c;
  --mist:#d3dfe6;
  --ink:#4a4a4a;
  --muted:#a9a9a9;
  --paper:#ffffff;
  --stage:#eef1f3;
  --panel-grey:#dcdcdc;
}
*{margin:0;padding:0;box-sizing:border-box}
html,body{width:1200px;height:1200px;overflow:hidden;background:var(--stage);font-family:'Inter',sans-serif}
.page{position:absolute;left:23px;top:0;width:1736px;height:1803px;transform:scale(0.6655);transform-origin:0 0;background:var(--paper);overflow:hidden}
.abs{position:absolute}
.announce{left:0;top:0;width:1736px;height:63px;background:var(--crimson);color:#fff;font-size:18px;display:flex;align-items:center;justify-content:center;letter-spacing:.2px}
.header{left:0;top:63px;width:1736px;height:135px;background:var(--paper)}
.brand{left:120px;top:28px;display:flex;align-items:center;gap:6px}
.brand-mark{width:80px;height:80px;border-radius:50%;background:var(--steel)}
.brand-name{color:var(--steel);font-weight:700;font-size:24px;line-height:1.05;letter-spacing:.5px}
.brand-name small{display:block;font-size:15px;font-weight:700;letter-spacing:.6px}
.nav{top:56px;font-size:19px;color:#5a5a5a;letter-spacing:.3px}
.search{left:1303px;top:54px}
.btn-head{left:1403px;top:37px;width:212px;height:61px;border-radius:31px;background:var(--steel);color:#fff;font-size:19px;display:flex;align-items:center;justify-content:center}
.usp{left:0;top:198px;width:1736px;height:85px;background:var(--mist)}
.usp-item{top:0;height:85px;display:flex;align-items:center;gap:8px;font-size:19px;color:var(--ink);letter-spacing:.3px;text-transform:uppercase}
.hero{left:0;top:283px;width:1736px;height:726px;background:var(--steel);overflow:hidden}
.photo{top:0;height:726px}
.hero-copy{left:134px;color:#fff}
.eyebrow{top:170px;font-size:19px;line-height:23px;text-transform:uppercase}
.headline{top:240px;font-size:74px;font-weight:800;letter-spacing:.5px;white-space:nowrap}
.lede{top:354px;width:600px;font-size:23.5px;line-height:29px}
.btn{top:496px;height:61px;border-radius:31px;font-size:19px;font-weight:600;display:flex;align-items:center;justify-content:center;color:#fff}
.btn-contact{left:134px;width:211px;background:var(--crimson);border:2px solid #fff}
.btn-call{left:365px;width:258px;border:2px solid #fff}
.trusted{left:0;top:1009px;width:1736px;height:269px;background:var(--paper)}
.trusted h2{position:absolute;top:62px;width:1736px;text-align:center;color:var(--muted);font-size:28px;font-weight:700;letter-spacing:.5px}
.client{background:#b9b9b9;border-radius:4px}
.benefits{left:0;top:1278px;width:868px;height:525px;background:var(--steel)}
.benefit{width:190px;text-align:center;color:#fff;font-size:19px;line-height:23px}
.media{left:868px;top:1278px;width:868px;height:525px;background:var(--panel-grey)}
.video{left:88px;top:189px;width:692px;height:400px;border-radius:22px;background:linear-gradient(160deg,#6a5f55,#3f3a35 55%,#8b8f93);overflow:hidden}
.play{left:292px;top:138px;width:110px;height:110px;border-radius:50%;background:var(--steel)}
</style>
</head>
<body>
<div class="page">

  <div class="abs announce">Free Site Surveys Available In March</div>

  <header class="abs header">
    <div class="abs brand">
      <div class="brand-mark"></div>
      <div class="brand-name">MARLOWFIELD'S<small>PVC SOLUTIONS LIMITED</small></div>
    </div>
    <span class="abs nav" style="left:634px">HOME</span>
    <span class="abs nav" style="left:751px">ALL PRODUCTS</span>
    <span class="abs nav" style="left:957px">ABOUT US</span>
    <span class="abs nav" style="left:1117px">RESOURCES</span>
    <svg class="abs search" width="28" height="28" viewBox="0 0 28 28" fill="none" stroke="#3a6f8c" stroke-width="2.4"><circle cx="12" cy="12" r="9"/><line x1="18.5" y1="18.5" x2="26" y2="26"/></svg>
    <div class="abs btn-head">CONTACT US</div>
  </header>

  <section class="abs usp">
    <div class="abs usp-item" style="left:120px"><svg width="50" height="34"><circle cx="25" cy="17" r="15" fill="#c63a51"/></svg>30+ Experienced</div>
    <div class="abs usp-item" style="left:502px"><svg width="50" height="50"><circle cx="25" cy="25" r="22" fill="#d66a7a"/></svg>Quality Assured</div>
    <div class="abs usp-item" style="left:883px"><svg width="58" height="32"><rect width="58" height="32" fill="#2f4f8f"/><rect y="12" width="58" height="8" fill="#c63a51"/></svg>Manufactured By Us</div>
    <div class="abs usp-item" style="left:1315px"><svg width="58" height="44" fill="none" stroke="#666" stroke-width="2.4"><circle cx="18" cy="22" r="15"/><circle cx="18" cy="22" r="6"/><circle cx="44" cy="22" r="11"/><circle cx="44" cy="22" r="4"/></svg>Project Management</div>
  </section>

  <section class="abs hero">
    <div class="abs photo" role="img" aria-label="Grey industrial curtain enclosure in a warehouse" style="left:730px;width:250px;background:linear-gradient(180deg,#9a9c9c,#7b7e80 60%,#a8a9a8)"></div>
    <div class="abs photo" role="img" aria-label="Red and grey PVC curtains dividing a factory floor" style="left:980px;width:260px;background:linear-gradient(180deg,#8a8c8f 0%,#c03a30 35%,#b8b9ba 70%,#d6d6d4)"></div>
    <div class="abs photo" role="img" aria-label="Clear blue PVC strip curtain" style="left:1240px;width:259px;background:linear-gradient(180deg,#8fbfae 0%,#c3c8ef 30%,#6f6fd0 75%,#9a9ad8)"></div>
    <div class="abs photo" role="img" aria-label="White sliding curtain on steel frame" style="left:1499px;width:237px;background:linear-gradient(180deg,#cfc6b8,#b8b1a6 60%,#8a7a66)"></div>
    <svg class="abs" style="left:0;top:0" width="1000" height="726"><path d="M0 0 H732 C860 130 905 290 885 470 C870 600 810 690 735 726 H0 Z" fill="#3a6f8c"/></svg>
    <div class="abs hero-copy eyebrow">Cut Cost, Control<br>Climate, Combat Dust</div>
    <h1 class="abs hero-copy headline">TRAXA CURTAIN</h1>
    <p class="abs hero-copy lede">Upgrade Your Industrial Space With Our Durable Sliding Industrial Curtains. Effortlessly Transform Your Workspace For Maximum Efficiency With Easy Installation And Versatile Applications.</p>
    <div class="abs btn btn-contact">CONTACT US</div>
    <div class="abs btn btn-call">CALL : 01632 960481</div>
  </section>

  <section class="abs trusted">
    <h2>TRUSTED BY GLOBAL COMPANIES</h2>
    <div class="abs client" style="left:137px;top:160px;width:60px;height:50px"></div>
    <div class="abs client" style="left:247px;top:160px;width:112px;height:50px"></div>
    <div class="abs client" style="left:410px;top:158px;width:120px;height:50px"></div>
    <div class="abs client" style="left:582px;top:160px;width:134px;height:50px"></div>
    <div class="abs client" style="left:765px;top:145px;width:92px;height:78px;border-radius:50%"></div>
    <div class="abs client" style="left:907px;top:145px;width:106px;height:76px"></div>
    <div class="abs client" style="left:1090px;top:165px;width:100px;height:38px;border-radius:50%"></div>
    <div class="abs client" style="left:1266px;top:147px;width:130px;height:72px"></div>
    <div class="abs client" style="left:1448px;top:141px;width:150px;height:84px"></div>
  </section>

  <section class="abs benefits">
    <svg class="abs" style="left:160px;top:175px" width="104" height="100" fill="#fff"><path d="M58 8 L100 16 C100 50 90 75 62 92 C42 78 36 60 36 40 Z"/><rect x="0" y="44" width="100" height="8" transform="rotate(40 50 48)"/></svg>
    <div class="abs benefit" style="left:117px;top:297px">Prevent Cross-Contamination</div>
    <svg class="abs" style="left:372px;top:175px" width="124" height="96" fill="#fff"><path d="M12 72 C12 38 34 16 56 12 V2 H68 V12 C92 16 112 38 112 72 Z"/><rect x="0" y="76" width="124" height="14" rx="7"/></svg>
    <div class="abs benefit" style="left:339px;top:297px">Protect Employees</div>
    <svg class="abs" style="left:610px;top:190px" width="94" height="60" fill="#fff"><rect x="0" y="14" width="24" height="6" rx="3"/><rect x="8" y="28" width="20" height="6" rx="3"/><rect x="0" y="42" width="24" height="6" rx="3"/><path d="M62 0 L90 14 V44 L62 58 L34 44 V14 Z"/></svg>
    <div class="abs benefit" style="left:561px;top:297px">Quick To Deploy</div>
    <svg class="abs" style="left:162px;top:410px" width="100" height="96"><circle cx="50" cy="50" r="30" fill="#fff"/><line x1="8" y1="4" x2="94" y2="92" stroke="#3a6f8c" stroke-width="14"/><line x1="8" y1="4" x2="94" y2="92" stroke="#fff" stroke-width="6"/></svg>
    <svg class="abs" style="left:392px;top:410px" width="84" height="96"><path d="M42 2 L82 16 C82 56 68 80 42 94 C16 80 2 56 2 16 Z" fill="#fff"/><rect x="38" y="28" width="8" height="36" fill="#3a6f8c"/><rect x="24" y="42" width="36" height="8" fill="#3a6f8c"/></svg>
    <svg class="abs" style="left:614px;top:410px" width="96" height="90"><rect x="4" y="4" width="74" height="74" rx="6" fill="none" stroke="#fff" stroke-width="8"/><rect x="4" y="50" width="30" height="28" fill="#fff"/><circle cx="70" cy="66" r="20" fill="#3a6f8c"/><circle cx="70" cy="66" r="15" fill="none" stroke="#fff" stroke-width="8" stroke-dasharray="6 4"/></svg>
  </section>

  <section class="abs media">
    <div class="abs video" role="img" aria-label="Video thumbnail of a retractable curtain booth in a workshop">
      <div class="abs play"></div>
      <svg class="abs" style="left:330px;top:170px" width="46" height="46"><path d="M6 2 L42 23 L6 44 Z" fill="#fff"/></svg>
    </div>
  </section>

</div>
</body>
</html>
```